We need a DL size flyer, double sided, for our lawn mowing and gardening business, Kestrel Greens.

We want to run on the front side, the following promotion:
50% off lawn mowing, applies to first lawn mowed on any regular service,
applies to first 100 callers only, so call now!
Professional lawn mowing at an affordable price.

Logo at the bottom left, with Lawn and Garden Maintenance written just below logo.

On bottom Right contact details;
Tom and Gareth
Ph: 0487650912
Email: kestrelgreens@mailbox-example.com
www.kestrelgreens-example.com.au

Front side positioned horizontally, with a bright and colour full design in the background, with the offer of 50% Off lawn mowing in large letters along the top.

On the rear side, also positioned horizontally, a list of our services, stating;

At Kestrel Greens we specialise in the following services;
Lawn mowing
Edging
Blowing
Hedging
Pruning
Tree Loping
Weeding
Poisoning
Mulching
Fertilising
Rubbish removal
Planting
Lawn care and advice
Turf
And any other garden maintenance job,
No job too big or too small.
(No particular order, whatever fits best)
Also include our contact details,
Kestrel Greens
Ph 0487650912
www.kestrelgreens-example.com.au

Target Market(s)

Home owners, aged between 30-50 years old, moderate socio ecenomic status to more afluent areas.

Industry/Entity Type

Business

Requirements
Must have
• DL size, front and back, full colour.
Nice to have
• The writting stating "Kestrel Greens" in our logo is quite bland, if that could also be amended to make it more appealing, but change the writting design only not the actual logo.

```html
<!DOCTYPE html>
<html lang="en">
<head>
<meta charset="utf-8">
<title>Kestrel Greens – DL Flyer Front</title>
<link rel="stylesheet" href="https://fonts.googleapis.com/css2?family=Anton&family=Oswald:wght@500;700&family=Arimo:ital,wght@0,400;0,700;1,700&display=swap">
<style>
  :root {
    --page-bg: #2b2b2b;
    --card-white: #ffffff;
    --brand-green: #14853a;
    --offer-yellow: #f7c600;
    --ink: #1b1b1b;
    --banner-edge: #1e2a10;
  }
  * { margin: 0; padding: 0; box-sizing: border-box; }
  html, body { width: 1200px; height: 900px; overflow: hidden; }
  body { background: var(--page-bg); position: relative; }

  .flyer {
    position: absolute; left: 87px; top: 194px;
    width: 1028px; height: 513px;
    background: var(--card-white);
  }

  .garden-photo {
    position: absolute; left: 22px; top: 21px;
    width: 983px; height: 364px;
    background:
      radial-gradient(ellipse 45% 40% at 45% 75%, #8fd14a 0%, rgba(143,209,74,0) 70%),
      radial-gradient(ellipse 30% 25% at 60% 80%, #cdbb95 0%, rgba(205,187,149,0) 70%),
      linear-gradient(180deg, #4e7d2f 0%, #3f7a2a 40%, #6fb23a 70%, #4f8f2c 100%);
  }

  .offer-panel {
    position: absolute; left: 613px; top: 36px;
    width: 392px; height: 282px;
    background: linear-gradient(160deg, #0f6b22 0%, #1f8a2e 45%, #0a4f18 100%);
    color: var(--offer-yellow);
  }
  .offer-headline {
    position: absolute; left: 22px; top: 4px;
    font-family: "Anton", sans-serif; font-size: 104px; line-height: 1.15;
    letter-spacing: 1px; font-weight: 400;
    text-shadow: 2px 2px 0 rgba(0,0,0,0.35);
  }
  .offer-terms {
    position: absolute; left: 22px; top: 128px;
    font-family: "Oswald", sans-serif; font-weight: 700;
    font-size: 19px; line-height: 27px;
    text-shadow: 1px 1px 0 rgba(0,0,0,0.4);
  }
  .offer-cta {
    position: absolute; left: 22px; top: 210px;
    font-family: "Anton", sans-serif; font-size: 54px; line-height: 1.1;
    color: #ffffff;
    text-shadow: 2px 2px 0 rgba(0,0,0,0.45);
  }

  .tagline-banner {
    position: absolute; left: 363px; top: 330px;
    width: 642px; height: 36px;
    background: var(--offer-yellow);
    border: 3px solid var(--banner-edge); border-right: none;
    border-radius: 18px 0 0 18px;
    font-family: "Arimo", sans-serif; font-weight: 700; font-style: italic;
    font-size: 18px; line-height: 30px;
    color: var(--ink); padding-left: 22px; white-space: nowrap;
  }

  .brand {
    position: absolute; left: 30px; top: 410px; width: 270px;
    text-align: center;
  }
  .brand-name {
    display: inline-flex; align-items: center; gap: 8px;
    font-family: "Arimo", sans-serif; font-weight: 700; font-size: 24px;
    color: var(--brand-green);
  }
  .brand-name::before {
    content: ""; width: 14px; height: 14px; background: var(--brand-green);
  }
  .brand-line {
    margin-top: 22px;
    font-family: "Arimo", sans-serif; font-weight: 700; font-size: 15px;
    color: var(--ink);
  }

  .call-block { position: absolute; left: 366px; top: 405px; white-space: nowrap; }
  .call-label {
    display: flex; align-items: center; gap: 8px;
    font-family: "Arimo", sans-serif; font-weight: 700; font-size: 38px;
    line-height: 42px; color: var(--brand-green);
  }
  .call-number {
    margin-top: 2px;
    font-family: "Arimo", sans-serif; font-weight: 700; font-size: 46px;
    line-height: 50px; color: var(--ink);
  }

  .divider {
    position: absolute; left: 687px; top: 405px;
    width: 2px; height: 87px; background: var(--ink);
  }

  .contact-block { position: absolute; left: 709px; top: 404px; width: 296px; }
  .owners {
    font-family: "Oswald", sans-serif; font-weight: 500; font-size: 34px;
    line-height: 40px; color: var(--brand-green);
    padding-bottom: 1px; border-bottom: 2px solid var(--ink);
    white-space: nowrap;
  }
  .contact-line {
    font-family: "Arimo", sans-serif; font-weight: 700; font-size: 14.5px;
    line-height: 21px; color: var(--ink); white-space: nowrap;
  }
  .owners + .contact-line { margin-top: 5px; }
</style>
</head>
<body>
  <main class="flyer">
    <div class="garden-photo" role="img" aria-label="Photograph of a landscaped garden with mown lawn, trees, shrubs and a winding gravel path"></div>

    <section class="offer-panel">
      <h1 class="offer-headline">50% off</h1>
      <p class="offer-terms">lawn mowing, applies to first<br>lawn mowed on any regular service,<br>applies to first 100 callers only.</p>
      <p class="offer-cta">SO CALL NOW!</p>
    </section>

    <p class="tagline-banner">PROFESSIONAL LAWN MOWING AT AN AFFORDABLE PRICE</p>

    <div class="brand">
      <p class="brand-name">Kestrel Greens</p>
      <p class="brand-line">Lawn and Garden Maintenance</p>
    </div>

    <div class="call-block">
      <p class="call-label">
        <svg width="48" height="34" viewBox="0 0 48 34" aria-hidden="true">
          <path d="M4 12 C4 4 44 4 44 12 L44 15 L34 15 L33 10 L15 10 L14 15 L4 15 Z" fill="var(--brand-green)"/>
          <path d="M12 17 L36 17 L42 32 L6 32 Z" fill="var(--brand-green)"/>
          <circle cx="24" cy="24" r="4" fill="#ffffff"/>
        </svg>
        CALL NOW!
      </p>
      <p class="call-number">048.765.0912</p>
    </div>

    <div class="divider"></div>

    <div class="contact-block">
      <p class="owners">Tom and Gareth</p>
      <p class="contact-line">kestrelgreens@mailbox-example.com</p>
      <p class="contact-line">www.kestrelgreens-example.com.au</p>
    </div>
  </main>
</body>
</html>
```